IronPeak 317

Brochure must include all info on the mock up of the brochure I have put together in Word. A similar design would be great but a little more professional would be great.

Industry/Entity Type

It Professional

Requirements
Must have
• MUST INCLUDE ALL INFORMATION IN MOCK UP

```html
<!DOCTYPE html>
<html lang="en">
<head>
<meta charset="utf-8">
<title>IronPeak 317 – Brochure</title>
<link href="https://fonts.googleapis.com/css2?family=Oswald:wght@400;500;600;700&display=swap" rel="stylesheet">
<style>
  :root {
    --bg-dark: #262626;
    --bg-mid: #353535;
    --accent: #f7c21b;
    --text: #ffffff;
    --divider: rgba(255,255,255,0.12);
  }
  * { margin: 0; padding: 0; box-sizing: border-box; }
  html, body { width: 1200px; height: 848px; overflow: hidden; background: var(--bg-dark); }
  .brochure {
    position: relative;
    width: 1200px; height: 848px;
    background: radial-gradient(ellipse at 50% 35%, var(--bg-mid) 0%, var(--bg-dark) 75%);
    font-family: "Oswald", "Arial Narrow", sans-serif;
    color: var(--text);
    overflow: hidden;
  }
  .panel {
    position: absolute; top: 0; width: 400px; height: 848px;
  }
  .panel--intro { left: 0; }
  .panel--signup { left: 400px; border-left: 1px solid var(--divider); border-right: 1px solid var(--divider); }
  .panel--prices { left: 800px; }
  .gym-photo {
    position: absolute; left: 0; top: 0; width: 400px; height: 600px;
  }
  .panel-title {
    position: relative;
    text-align: center;
    text-transform: uppercase;
    font-weight: 700;
    font-size: 25px;
    line-height: 26px;
    padding-top: 36px;
    letter-spacing: 0.5px;
  }
  .panel-title .accent { color: var(--accent); display: block; }
  .panel-title .sub { display: block; }
  .intro-body {
    position: absolute; left: 16px; top: 104px; width: 370px;
    font-size: 15.2px; font-weight: 500; line-height: 26.6px;
    text-align: justify; hyphens: auto;
  }
  .intro-body p + p { margin-top: 26px; }
  .intro-body p.tight { margin-top: 0; }
  .step {
    position: absolute; left: 16px; width: 368px;
    font-size: 15.2px; font-weight: 500; line-height: 26.6px;
    text-align: justify;
  }
  .step-label { color: var(--accent); font-weight: 600; font-size: 16px; display: block; margin-bottom: 10px; }
  .price {
    position: absolute; left: 14px; width: 380px;
    font-size: 16.5px; font-weight: 500; line-height: 28px;
  }
  .price-name { color: var(--accent); display: block; padding-left: 6px; }
  .price-name::before { content: "•"; margin-right: 10px; }
  .price-note { display: block; }
</style>
</head>
<body>
<div class="brochure">

  <section class="panel panel--intro">
    <h2 class="panel-title"><span class="accent">Our ‘On - Ramp’ Program</span><span class="sub">For Beginners</span></h2>
    <div class="intro-body">
      <p>The emphasis in the On-Ramp program is on skill development and exposure to our basic movements. It is designed to prepare beginners, or those who have not done PeakFit before, to enter our ongoing group classes. In the program we be hammering technique— both to ensure your safety—and success at the next level.”</p>
      <p>It is a program that involves 8 sessions. In these sessions we will introduce you to technique and mechanics first, then intensity. We will explain how to understand our daily WOD ( Workout Of the Day) which is written up on our whiteboard and found on our website. We will be showing you movements that begin with the relatively non technical movements and then move on to progressively more technical.</p>
      <p class="tight">There will be a workout at the end of each session which will get progressively more challenging as the course progresses.</p>
      <p class="tight">The difficulty of these workouts is ultimately in your hands…the degree that you push yourself will determine how much suffering goes on.</p>
      <p>The class is called “On Ramp” for a specific reason…we want to ramp you up to the level of intensity and output that is inherent in our group classes.</p>
    </div>
  </section>

  <section class="panel panel--signup">
    <svg class="gym-photo" role="img" aria-label="Gym interior with punching bags and training equipment" viewBox="0 0 400 600">
      <defs>
        <linearGradient id="photoTone" x1="0" y1="0" x2="0" y2="1">
          <stop offset="0" stop-color="#4a4a4a"/>
          <stop offset="0.45" stop-color="#5a4a48"/>
          <stop offset="1" stop-color="#2e2e2e" stop-opacity="0"/>
        </linearGradient>
      </defs>
      <rect width="400" height="600" fill="url(#photoTone)"/>
    </svg>
    <h2 class="panel-title"><span class="accent">How Do I Sign Up?</span><span class="sub">A Step By Step Guide</span></h2>
    <div class="step" style="top:106px"><span class="step-label">STEP 1</span>The first step is to go to our home page at www.ironpeak-training.com</div>
    <div class="step" style="top:232px"><span class="step-label">STEP 2</span>Under the “Membership” tab click on “Sign Up”</div>
    <div class="step" style="top:326px"><span class="step-label">STEP 3</span>Select “On-Ramp Program” or if you have PeakFit experience you can select one of our other memberships</div>
    <div class="step" style="top:471px"><span class="step-label">STEP 4</span>Once you have entered your email address you will be sent a password</div>
    <div class="step" style="top:591px"><span class="step-label">STEP 5</span>Once that is done you can go into your account and enter your payment details or pay the next time you are in.</div>
    <div class="step" style="top:736px"><span class="step-label">STEP 6</span>Using your email address and password you can now book into the classes you wish to attend</div>
  </section>

  <section class="panel panel--prices">
    <h2 class="panel-title"><span class="accent">Memberships</span><span class="sub">Types and Prices</span></h2>
    <div class="price" style="top:104px"><span class="price-name">Monthly Unlimited = $200</span><span class="price-note">(Unlimited classes for a month)</span></div>
    <div class="price" style="top:176px"><span class="price-name">Monthly (3 Days Per Week) = $155</span><span class="price-note">(3 classes per week)</span></div>
    <div class="price" style="top:268px"><span class="price-name">On-Ramp Beginners Program = $100</span><span class="price-note">(8 classes- 1 Month Limit - one time only offer)</span></div>
    <div class="price" style="top:350px"><span class="price-name">Transition Program = $130</span><span class="price-note">(8 Sessions - 1 Month limit)</span></div>
    <div class="price" style="top:432px"><span class="price-name">20-Class Pass = $370</span><span class="price-note">20 classes ($18.50/class)</span></div>
    <div class="price" style="top:514px"><span class="price-name">10 Class Pass = $200</span><span class="price-note">10 classes ($20/class)</span></div>
    <div class="price" style="top:596px"><span class="price-name">Drop-In = $25</span><span class="price-note">(Must Have PeakFit Experience)</span></div>
    <div class="price" style="top:678px"><span class="price-name">12 Month unlimited = $1,800</span><span class="price-note">Unlimited Membership (Unlimited classes)</span></div>
    <div class="price" style="top:760px"><span class="price-name">6 Month =unlimited = $1,000</span><span class="price-note">Unlimited Membership (Unlimited classes)</span></div>
  </section>

</div>
</body>
</html>
```